Re-design of website

I have an existing website that I would like to improve. The functionality will remain the same but the overall look will need to be changed. I have some ideas of what i would like included and am also in need of someone else to input their own creative ideas. I am on a tight deadline to get these improvements made as I have many people being directed to the site via our advertising campaigns that are in full swing late next week. Thanks
Target Market(s)
The website provides a virtual space for families to learn more about our learning program which we operate out of Dubai and will soon spread to the other Emirates. The families are generally between 25-50 year old parents with children up to the age of 6. They are local Emirati's as well as expats.

```html
<!DOCTYPE html>
<html lang="en">
<head>
<meta charset="utf-8">
<title>Bright Sprouts – Accelerated Learning Centre</title>
<link href="https://fonts.googleapis.com/css2?family=Ubuntu:wght@400;500&display=swap" rel="stylesheet">
<style>
  :root {
    --brand-blue: #0a7bc1;
    --sky-top: #bfe3fb;
    --sky-mid: #ffffff;
    --sky-band: #a9d6f5;
    --panel-bg: #eef5fd;
    --panel-border: #c3cbd4;
    --text-dark: #2e2e2e;
    --caption-grey: #8d9a9a;
    --footer-text: #17365f;
    --logo-navy: #1c4a6e;
    --sand: #f2cf3a;
    --hill: #b98a5c;
    --neuron-red: #e0262e;
  }
  * { box-sizing: border-box; margin: 0; padding: 0; }
  html, body { width: 1200px; height: 1192px; overflow: hidden; }
  body {
    position: relative;
    font-family: "Ubuntu", sans-serif;
    background: linear-gradient(180deg, var(--sky-top) 0%, var(--sky-mid) 30%, var(--sky-mid) 50%, #d9ecfa 68%, var(--sky-band) 76%, #cfe8fa 86%, #e6f3fc 100%);
  }
  .top-rule { position: absolute; left: 0; top: 0; width: 1200px; height: 10px; background: var(--brand-blue); }

  .sky-art {
    position: absolute; left: 90px; top: 14px; width: 1025px; height: 130px;
    border-radius: 65px;
    background: radial-gradient(ellipse at 55% 20%, rgba(230,120,90,0.35) 0%, rgba(150,210,120,0.25) 25%, rgba(120,195,245,0.55) 55%, rgba(255,255,255,0) 80%);
  }
  .logo {
    position: absolute; left: 130px; top: 150px; display: flex; align-items: center; gap: 12px;
  }
  .logo-dot { width: 34px; height: 34px; border-radius: 50%; background: var(--logo-navy); }
  .logo-name { font-size: 28px; font-weight: 500; color: var(--logo-navy); }

  .kids-art {
    position: absolute; left: 405px; top: 125px; width: 685px; height: 200px;
    border-radius: 16px;
    background: linear-gradient(90deg, #f6d8c4 0%, #e9ecd8 30%, #f7e4c8 55%, #f4d2b8 80%, #f0e0cf 100%);
    opacity: 0.85;
  }

  .main-nav {
    position: absolute; left: 106px; top: 376px; width: 988px; height: 38px;
    background: var(--brand-blue); border-radius: 8px;
    display: flex; justify-content: center; align-items: center; gap: 31px;
  }
  .main-nav a { color: #fff; text-decoration: none; font-size: 18px; }

  .content-panel {
    position: absolute; left: 104px; top: 449px; width: 989px; height: 502px;
    background: var(--panel-bg); border: 1px solid var(--panel-border); border-radius: 8px;
    overflow: hidden;
  }
  .intro-copy { position: absolute; left: 33px; top: 53px; width: 530px; }
  .intro-copy p { font-size: 15px; line-height: 24px; color: var(--text-dark); margin-bottom: 24px; }
  .panel-divider {
    position: absolute; left: 595px; top: 0; width: 14px; height: 100%;
    background: linear-gradient(90deg, #c8d3de 0%, #e2eaf3 60%, rgba(238,245,253,0) 100%);
  }
  .brain-figure { position: absolute; left: 650px; top: 52px; width: 300px; }
  .brain-sections { display: flex; gap: 9px; }
  .brain-section {
    width: 148px; height: 256px; border: 2px solid #c9706e;
  }
  .brain-section.stimulated { background: linear-gradient(160deg, #f4b3b5, #e9797d 50%, #f3adb0); }
  .brain-section.unstimulated { background: linear-gradient(160deg, #f8e4e7, #f1c3c7 50%, #f9e7ea); width: 142px; }
  .brain-captions { display: flex; gap: 9px; margin-top: 9px; }
  .brain-captions span {
    width: 148px; text-align: center; font-family: Arial, Helvetica, sans-serif;
    font-size: 16px; line-height: 19px; color: var(--caption-grey);
  }

  .site-footer { position: absolute; left: 130px; top: 988px; font-family: Arial, Helvetica, sans-serif; font-size: 12.5px; color: var(--footer-text); line-height: 24px; }
  .site-footer .copyright { padding-left: 3px; }
  .social-links { position: absolute; left: 897px; top: 999px; display: flex; gap: 9px; }
  .social-links a { width: 28px; height: 28px; border-radius: 50%; display: block; }
  .social-links a:nth-child(1) { background: #3b5f9e; }
  .social-links a:nth-child(2) { background: #3a9fd8; }
  .social-links a:nth-child(3) { background: #cf3b2c; }
  .social-links a:nth-child(4) { background: #3a87b9; }
  .social-links a:nth-child(5) { background: #cc2127; }

  .desert-art {
    position: absolute; left: 0; top: 1055px; width: 1200px; height: 137px;
    background: linear-gradient(180deg, rgba(180,220,245,0) 0%, #c9a57a 22%, var(--hill) 40%, #f5e16a 62%, var(--sand) 82%, #e9a521 100%);
  }
</style>
</head>
<body>
  <div class="top-rule"></div>
  <div class="sky-art" role="img" aria-label="Rainbow arching over soft blue clouds"></div>

  <header>
    <div class="logo">
      <span class="logo-dot"></span>
      <span class="logo-name">Bright Sprouts</span>
    </div>
    <div class="kids-art" role="img" aria-label="Illustration of a row of cheerful cartoon children, some in costumes"></div>
  </header>

  <nav class="main-nav">
    <a href="#">Home</a>
    <a href="#">Our Method</a>
    <a href="#">The Program</a>
    <a href="#">Media</a>
    <a href="#">Locations</a>
    <a href="#">About us</a>
    <a href="#">Contact</a>
    <a href="#">News &amp; Events</a>
  </nav>

  <main class="content-panel">
    <div class="intro-copy">
      <p>Research and leading academics agree that the early years of a child's life (defined as the 6 month old to 6 year old age group) is a critical time period to enhance the emotional and intellectual IQ of a child. 80% of your child's brain is developed by the age of 6 years old, to not offer heightened stimulation and specifically, right brain training during this period means that your child will not use a high proportion of their brain in their life time.</p>
      <p>Bright Sprouts Accelerated Learning Centre is the first a whole brain training program designed to maximise your child's potential during this key period of development.</p>
      <p>At Bright Sprouts, our philosophy and curriculum supports like-minded parents who want happiness for their children and want to see their children become the best they can be in their life. Our children are happy, confident and content with inquisitive minds and life skills that form the foundation of their lifetime of development and learning.</p>
    </div>
    <div class="panel-divider"></div>
    <figure class="brain-figure">
      <div class="brain-sections">
        <div class="brain-section stimulated" role="img" aria-label="Dense network of red neurons in a stimulated brain"></div>
        <div class="brain-section unstimulated" role="img" aria-label="Sparse network of red neurons in an unstimulated brain"></div>
      </div>
      <figcaption class="brain-captions">
        <span>section of a<br>stimulated brain</span>
        <span>section of a<br>unstimulated brain</span>
      </figcaption>
    </figure>
  </main>

  <footer class="site-footer">
    <div class="tel">Tel: +971 550 123 456</div>
    <div class="copyright">© 2013 Bright Sprouts</div>
  </footer>
  <div class="social-links">
    <a href="#" aria-label="Social profile 1"></a>
    <a href="#" aria-label="Social profile 2"></a>
    <a href="#" aria-label="Social profile 3"></a>
    <a href="#" aria-label="Social profile 4"></a>
    <a href="#" aria-label="Social profile 5"></a>
  </div>

  <div class="desert-art" role="img" aria-label="Cartoon desert with cacti, brown hills and yellow sand dunes"></div>
</body>
</html>
```